Geschäftspapiere für Kanzlei
Zielgruppe
Forschungsinstitute und Großunternehmen die eigene Entwicklungsabteilungen haben und Erfindungen patentieren lassen.
Aufgabenstellung
Möglicherweise ergibt eine Weiterentwiklung unseres logos Sinn? Denkbar wäre für uns aber auch auf das Logo ganz zu verzichten.
Es sollte nicht mehr als eine Farbe (Blauton) verwendet werden. Wir wollen schlicht, klassisch und seriös auftreten.

```html
<!DOCTYPE html>
<html lang="de">
<head>
<meta charset="utf-8">
<title>Briefbogen Patentanwaltskanzlei Dr. Keradze</title>
<link rel="stylesheet" href="https://fonts.googleapis.com/css2?family=Open+Sans:wght@400;600&family=Arimo:wght@400&display=swap">
<style>
  :root {
    --brand-blue: #1b2a78;
    --ink: #2b2b2b;
    --body-grey: #5a5a5a;
    --rule: #9a9a9a;
    --paper: #ffffff;
    --backdrop: #e6e6e6;
  }
  * { margin: 0; padding: 0; box-sizing: border-box; }
  html, body { width: 1151px; height: 1200px; overflow: hidden; background: var(--backdrop); }
  .sheet {
    position: absolute; left: 151px; top: 0; width: 849px; height: 1200px;
    background: var(--paper); font-family: "Open Sans", sans-serif; color: var(--ink);
  }
  .fold-mark { position: absolute; left: 0; width: 25px; height: 1px; background: #c8c8c8; }
  .brand-name {
    position: absolute; left: 101px; top: 40px;
    font-family: "Open Sans", sans-serif; font-weight: 600; font-size: 22px;
    letter-spacing: 0.5px; color: var(--brand-blue); text-transform: uppercase;
  }
  .sender-block {
    position: absolute; left: 524px; top: 44px; height: 198px;
    border-left: 1px solid var(--ink); padding-left: 16px;
    font-size: 12.4px; line-height: 17.6px;
  }
  .sender-block .address { margin-top: 12px; }
  .sender-block .contact { margin-top: 9px; list-style: none; }
  .sender-block .contact li { display: flex; align-items: center; gap: 9px; }
  .sender-block .contact svg { width: 12px; height: 12px; fill: var(--brand-blue); flex: none; }
  .return-line {
    position: absolute; left: 101px; top: 205px; font-size: 8.4px;
    border-bottom: 1px solid var(--ink); padding-bottom: 1px;
  }
  .letter-date { position: absolute; left: 524px; top: 252px; font-size: 12.4px; }
  .letter-body {
    position: absolute; left: 101px; top: 437px; width: 687px;
    font-family: "Arimo", sans-serif; font-size: 14.6px; line-height: 20px; color: var(--body-grey);
  }
  .reference { line-height: 17.6px; }
  .salutation { margin-top: 23px; }
  .letter-body p.paragraph { margin-top: 20px; text-align: justify; }
  .closing {
    position: absolute; left: 101px; top: 855px;
    font-family: "Arimo", sans-serif; font-size: 14.6px; color: var(--body-grey);
  }
  .signature { position: absolute; left: 93px; top: 886px; width: 192px; height: 62px; }
  .signer { position: absolute; left: 101px; top: 955px; font-size: 13px; }
  .footer {
    position: absolute; left: 0; right: 0; top: 1143px; text-align: center;
    font-size: 11px; line-height: 17.6px;
  }
</style>
</head>
<body>
<main class="sheet">
  <span class="fold-mark" style="top:425px"></span>
  <span class="fold-mark" style="top:599px"></span>
  <span class="fold-mark" style="top:849px"></span>

  <header>
    <div class="brand-name">Dr. Levan Keradze</div>

    <address class="sender-block" style="font-style:normal">
      <div>Dr. rer. nat. Levan Keradze, PhD<br>Patentanwalt<br>European Patent Attorney<br>European Design- und Trademark Attorney</div>
      <div class="address">Lindenhofstrasse 22<br>80335 München</div>
      <ul class="contact">
        <li><svg viewBox="0 0 12 12"><path d="M2.5 1h2l1 3-1.3 1a6 6 0 0 0 2.8 2.8L8 6.5l3 1v2A1.5 1.5 0 0 1 9.5 11 8.5 8.5 0 0 1 1 2.5 1.5 1.5 0 0 1 2.5 1z"/></svg>+ 49 89 310 447 120</li>
        <li><svg viewBox="0 0 12 12"><rect x="3" y="1" width="6" height="3"/><rect x="1" y="4.5" width="10" height="4.5" rx="1"/><rect x="3" y="8" width="6" height="3"/></svg>+ 49 89 310 447 19</li>
        <li><svg viewBox="0 0 12 12"><path d="M1 2.5h10v7H1z M1.5 3 6 6.5 10.5 3" stroke="#fff" stroke-width="0.8"/></svg>office@keradze-ip.de</li>
        <li><svg viewBox="0 0 12 12"><circle cx="6" cy="6" r="5.2"/><path d="M1 6h10M6 1c-2 2.6-2 7.4 0 10M6 1c2 2.6 2 7.4 0 10" stroke="#fff" stroke-width="0.7" fill="none"/></svg>www.keradze-ip.de</li>
      </ul>
    </address>

    <div class="return-line">Kanzlei Dr. Keradze | Lindenhofstrasse 22 | 80335 München</div>
    <div class="letter-date">München, den 24. September 2020</div>
  </header>

  <section class="letter-body">
    <div class="reference">Ihr Aktenzeichen:<br>Unser Aktenzeichen:</div>
    <p class="salutation">Sehr geehrte Damen und Herren,</p>
    <p class="paragraph">Sehr geehrter Herr Mustermann, jeder Setzer hat für diesen Zweck immer etwas Blindtext parat. Blindtext ist im Umfang von einigen tausend Anschlägen, der für die »äußerliche« Gestaltung einer Publikation verwendet und dessen Inhalt unwichtig ist. Man setzt ihn oft zum Beispiel in verschiedenen Schriften und Schriftgrößen, um anderen zu zeigen, wie eine bestimmte Schrift wirkt.</p>
    <p class="paragraph">Sehr geehrter Herr Mustermann, jeder Setzer hat für diesen Zweck immer etwas Blindtext parat. Blindtext ist im Umfang von einigen tausend Anschlägen, der für die »äußerliche« Gestaltung einer Publikation verwendet und dessen Inhalt unwichtig ist. Man setzt ihn oft zum Beispiel in verschiedenen Schriften und Schriftgrößen, um anderen zu zeigen, wie eine bestimmte Schrift wirkt.</p>
  </section>

  <div class="closing">Mit freundlichen Grüßen</div>
  <svg class="signature" role="img" aria-label="Handschriftliche Unterschrift von Dr. Levan Keradze" viewBox="0 0 192 62">
    <rect width="192" height="62" rx="4" fill="#e9ebf4"/>
  </svg>
  <div class="signer">Dr. Levan Keradze</div>

  <footer class="footer">
    Patentanwaltskanzlei Dr. Keradze • Steuernummer.: 143/208/55317 • Umsatzsteuer-ID-Nr.: DE 312774591<br>
    Nordbank Finanz NBF • IBAN: DE83700100800456123907 • BIC: NBFIDEM1XXX
  </footer>
</main>
</body>
</html>
```